New custom software business needs a Wordpress site

We need a Wordpress site for a new company based out of Chicago called 'Vellora Consulting'. Using a mix of on and off-shore resources we build custom software solutions, mainly focusing on small to medium sized companies. We help our customers "aspire" to do great things.
We have a basic site up here: https://brindlewave.example/. We worked on the content for it but not the branding. For now, this houses all the pages (except for a Contact Us page we'll be adding soon) for the foreseeable future.
We also have a new logo (attached) that we'd like to base the styling/colors on.
Target Market(s)
Small to medium sized companies that require tech resources
Industry/Entity Type
Software
Nice to have
- Teamwork, tech, professional but not elitist

```html
<!DOCTYPE html>
<html lang="en">
<head>
<meta charset="utf-8">
<title>Vellora Consulting — Custom Software Solutions</title>
<link href="https://fonts.googleapis.com/css2?family=Montserrat:wght@400;500;600;700&display=swap" rel="stylesheet">
<style>
:root{
  --navy:#06122b;
  --navy-2:#0b2550;
  --blue:#3a86cf;
  --blue-deep:#0d57b3;
  --blue-soft:#eaf2fb;
  --ink:#1d1d1f;
  --text:#555a63;
  --muted:#8b9099;
  --line:#dfe5ee;
  --white:#ffffff;
}
*{box-sizing:border-box;margin:0;padding:0}
html,body{width:1200px;height:4175px;overflow:hidden}
body{position:relative;font-family:"Montserrat",sans-serif;color:var(--text);background:var(--white)}
.abs{position:absolute}
.center{left:0;width:1200px;text-align:center}
.eyebrow{font-size:9px;font-weight:600;letter-spacing:3px;color:var(--blue);text-transform:uppercase}
.eyebrow.dash::before,.eyebrow.dash::after{content:"";display:inline-block;width:14px;height:1px;background:var(--blue);vertical-align:middle;margin:0 10px}
.title{font-weight:700;color:var(--ink);text-transform:uppercase;letter-spacing:.5px}
.lead{font-size:11.5px;line-height:1.65;color:var(--text)}
.btn{display:flex;align-items:center;justify-content:center;border-radius:16px;font-size:8.5px;font-weight:600;letter-spacing:1.2px;text-transform:uppercase;color:var(--white);background:var(--blue)}
.brand{display:flex;align-items:center;gap:10px;color:var(--white)}
.brand-dot{width:26px;height:26px;border-radius:50%;background:var(--blue)}
.brand-name{font-size:15px;font-weight:600;letter-spacing:.5px}

/* hero */
.hero{top:0;left:0;width:1200px;height:592px;background:radial-gradient(ellipse 700px 260px at 820px 440px,#1d4f8e 0%,#0c2a58 40%,rgba(6,18,43,0) 75%),linear-gradient(180deg,#040b1c 0%,#071a3a 60%,#0a2552 100%)}
.nav{top:22px;left:130px;width:940px;height:36px;display:flex;align-items:center}
.menu{position:absolute;left:340px;display:flex;gap:16px;font-size:9.5px;font-weight:700;color:var(--white);letter-spacing:.4px}
.menu .active{color:var(--blue);border-bottom:2px solid var(--blue);padding-bottom:4px}
.phone{position:absolute;left:705px;font-size:9.5px;font-weight:600;color:var(--white);display:flex;align-items:center;gap:6px}
.phone::before{content:"";position:absolute;left:-16px;width:1px;height:12px;background:rgba(255,255,255,.4)}
.nav .btn{position:absolute;right:0;width:113px;height:24px}
.hero h1{top:215px;font-size:39px;line-height:44px;color:var(--white);font-weight:600;letter-spacing:1px}
.hero .eyebrow{top:190px;color:var(--white);font-size:8.5px}
.hero .lead{top:316px;left:335px;width:530px;color:var(--white);font-size:10.5px;text-align:center}
.hero .btn{top:383px;left:539px;width:122px;height:28px;background:var(--white);color:var(--ink)}

/* about */
.photo{border-radius:16px}
.about-img{top:654px;left:130px;width:460px;height:308px;background:linear-gradient(135deg,#e9e6e1,#b9b4ae 55%,#6b6660)}
.play{top:776px;left:560px;width:60px;height:60px;border-radius:50%;background:var(--blue-deep);box-shadow:0 0 0 8px rgba(255,255,255,.85);display:flex;align-items:center;justify-content:center}
.about-text{top:660px;left:690px;width:380px}
.about-text h2{font-size:31px;line-height:36px;margin:14px 0 12px}
.about-text .lead{font-size:10.5px;margin-bottom:10px}
.about-text .btn{width:128px;height:28px;margin-top:22px}

/* stats */
.divider{top:1025px;left:0;width:1200px;height:1px;background:var(--line)}
.divider-label{top:1018px;left:540px;width:120px;background:var(--white);text-align:center}
.stat{top:1089px;width:200px;text-align:center}
.stat .ic{width:62px;height:62px;margin:0 auto;border-radius:50%;background:var(--blue-soft);display:flex;align-items:center;justify-content:center}
.stat .ic.on{background:var(--blue-deep)}
.stat .num{font-size:30px;font-weight:700;color:var(--ink);margin-top:10px;letter-spacing:1px}
.stat .num.on{color:var(--blue)}
.stat .lbl{font-size:10px;color:var(--text);margin-top:4px}

/* services */
.services{top:1290px;left:0;width:1200px;height:738px;background:linear-gradient(180deg,#eaf1fa 0%,#f4f8fd 70%,#ffffff 100%)}
.section-title{font-size:31px}
.card{top:1508px;width:302px;height:438px;border-radius:14px;overflow:hidden}
.card-code{left:130px;background:linear-gradient(160deg,#0e1a2c,#1f3350 50%,#0c1422)}
.card-staff{left:449px;background:linear-gradient(170deg,#3a3a3c,#262628 60%,#1b1b1c)}
.card-support{left:769px;background:linear-gradient(150deg,#e7ebf0,#c5ccd5 60%,#9aa3ad)}
.card-label{position:absolute;bottom:52px;left:0;width:100%;text-align:center;font-size:9.5px;font-weight:600;color:var(--white);letter-spacing:.3px}
.card-badge{top:1930px;width:34px;height:34px;border-radius:50%;background:var(--white);display:flex;align-items:center;justify-content:center}
.staff-inner{position:absolute;top:30px;left:28px;width:246px;text-align:center;color:var(--white)}
.staff-inner .mark{width:34px;height:34px;margin:0 auto;border-radius:50%;background:rgba(255,255,255,.9)}
.staff-inner h3{font-size:15px;font-weight:600;margin:14px 0 10px}
.staff-inner p{font-size:10px;line-height:1.55}
.staff-inner .btn{width:110px;height:28px;margin:12px auto 0}

/* testimonials */
.testimonials{top:2028px;left:0;width:1200px;height:408px;background:linear-gradient(90deg,#4d5560 0%,#2c333c 35%,#222a34 65%,#6d747c 100%)}
.testimonials .shade{position:absolute;inset:0;background:rgba(10,14,22,.35)}
.avatar{top:2186px;left:574px;width:52px;height:52px;border-radius:50%;background:linear-gradient(135deg,#c9ccd1,#7d848d);border:2px solid var(--white)}
.quote{top:2252px;left:260px;width:680px;text-align:center;color:var(--white);font-size:12.5px;line-height:19px}
.stars{top:2316px;letter-spacing:4px;font-size:10px;color:var(--blue)}
.person{top:2337px;color:var(--white);font-size:10px;line-height:16px}
.person b{font-weight:700}

/* approach */
.step{top:2623px;width:140px;text-align:center}
.step .ic{width:62px;height:62px;margin:0 auto;border-radius:50%;background:#151515;display:flex;align-items:center;justify-content:center}
.step .ic.on{background:var(--blue)}
.step .lbl{font-size:9px;font-weight:600;letter-spacing:.6px;color:var(--muted);margin-top:20px;text-transform:uppercase}
.step .lbl.on{color:var(--blue)}

/* team */
.team{top:2883px;left:0;width:1200px;height:714px;background:linear-gradient(180deg,#eaf1fa 0%,#f6f9fd 60%,#eef3fa 100%)}
.member{top:3097px;width:200px;text-align:center}
.member .pic{width:172px;height:172px;margin:0 auto;border-radius:50%;border:5px solid var(--white);box-shadow:0 2px 10px rgba(0,0,0,.08)}
.member .name{font-size:11.5px;font-weight:700;color:var(--ink);letter-spacing:.8px;margin-top:12px;text-transform:uppercase}
.member .name.on{color:var(--blue)}
.member .role{font-size:8px;color:var(--muted);margin-top:6px;text-transform:uppercase}
.bio{top:3170px;left:579px;width:42px;height:16px;border-radius:3px;background:#111;color:var(--white);font-size:7px;display:flex;align-items:center;justify-content:center}
.cert{top:3462px;width:162px;height:65px;background:rgba(255,255,255,.55);display:flex;align-items:center;justify-content:center}
.cert.on{background:var(--white);box-shadow:0 2px 10px rgba(0,0,0,.12)}
.cert .shape{background:#b8bdc5}

/* cta */
.cta{top:3597px;left:0;width:1200px;height:279px;background:linear-gradient(100deg,#0a1a33 0%,#173a6a 45%,#2b4f7a 60%,#10233f 100%)}
.cta .title{color:var(--white)}
.cta .lead{color:var(--white)}

/* footer */
.footer{top:3876px;left:0;width:1200px;height:299px;background:var(--blue-deep)}
.foot-brand{top:3940px;left:0;width:1200px;display:flex;flex-direction:column;align-items:center;gap:10px;color:var(--white)}
.foot-brand .brand-dot{width:50px;height:50px;background:rgba(255,255,255,.25);border:2px solid var(--white)}
.foot-brand .brand-name{font-size:20px;font-weight:500}
.copy{top:4044px;font-size:8px;color:rgba(255,255,255,.75);letter-spacing:.5px}
.foot-links{top:4064px;font-size:8px;font-weight:600;color:var(--white);letter-spacing:.5px}
.foot-links span{margin:0 10px}
.social{top:4088px;left:0;width:1200px;display:flex;justify-content:center;gap:14px;align-items:center}
.social i{display:block;width:12px;height:12px;border-radius:50%;background:rgba(255,255,255,.8)}
.social i.on{width:24px;height:24px;background:var(--blue)}
</style>
</head>
<body>

<!-- HERO -->
<section class="abs hero" role="img" aria-label="Dark blue abstract digital particle wave background"></section>
<nav class="abs nav">
  <div class="brand"><span class="brand-dot"></span><span class="brand-name">VELLORA CONSULTING</span></div>
  <div class="menu"><span class="active">HOME</span><span>ABOUT</span><span>SERVICES</span><span>APPROACH</span><span>TEAM</span><span>CONTACT US</span></div>
  <div class="phone"><svg width="10" height="10" viewBox="0 0 24 24" fill="none" stroke="#fff" stroke-width="2.4"><path d="M22 16.9v3a2 2 0 0 1-2.2 2A19.8 19.8 0 0 1 2.1 4.2 2 2 0 0 1 4.1 2h3a2 2 0 0 1 2 1.7l.5 3a2 2 0 0 1-.6 1.8L7.7 9.8a16 16 0 0 0 6.5 6.5l1.3-1.3a2 2 0 0 1 1.8-.6l3 .5a2 2 0 0 1 1.7 2z"/></svg>+012 555 0142</div>
  <div class="btn">&#9634;&nbsp; GET STARTED</div>
</nav>
<div class="abs center eyebrow hero-eyebrow" style="top:190px;color:#fff;font-size:8.5px">Custom Solution Delivery</div>
<h1 class="abs center" style="top:215px;font-size:39px;line-height:44px;color:#fff;font-weight:600;letter-spacing:1px">HIGH-QUALITY<br>SOFTWARE SOLUTION</h1>
<p class="abs lead" style="top:316px;left:335px;width:530px;color:#fff;font-size:10.5px;text-align:center">Welcome to Vellora, a software consulting company specializing in serving small to medium size businesses. We understand the unique challenges and opportunities that these companies face, and we are dedicated to helping them succeed through innovative technology solutions.</p>
<div class="abs btn" style="top:383px;left:539px;width:122px;height:28px;background:#fff;color:#1d1d1f">Explore More</div>
<svg class="abs" style="top:570px;left:594px" width="12" height="8" viewBox="0 0 12 8"><path d="M1 1l5 5 5-5" fill="none" stroke="#fff" stroke-width="1.5"/></svg>

<!-- ABOUT -->
<div class="abs photo about-img" role="img" aria-label="Photo of developers working together at computers in an office"></div>
<div class="abs play"><svg width="16" height="16" viewBox="0 0 16 16"><path d="M5 3l8 5-8 5z" fill="none" stroke="#fff" stroke-width="1.4"/></svg></div>
<div class="abs about-text">
  <div class="eyebrow">About</div>
  <h2 class="title">Vellora<br>Consulting</h2>
  <p class="lead">Our team of experienced professionals has a diverse range of skills and expertise, making us well-equipped to handle any project, big or small. We specialize in custom software development, working closely with our clients to understand their specific needs and build solutions that meet their requirements.</p>
  <p class="lead">From developing web and mobile applications to implementing cloud-based systems and integrating with existing platforms, we have the tools and knowledge to deliver results that drive success.</p>
  <div class="btn">More About Us</div>
</div>

<!-- EXPERIENCE -->
<div class="abs divider"></div>
<div class="abs divider-label eyebrow">Experience</div>
<div class="abs stat" style="left:140px"><div class="ic"><svg width="24" height="24" viewBox="0 0 24 24" fill="none" stroke="#3a86cf" stroke-width="1.6"><rect x="3" y="5" width="18" height="16" rx="2"/><path d="M3 10h18M8 3v4M16 3v4"/><circle cx="16" cy="16" r="2.5"/></svg></div><div class="num">35</div><div class="lbl">Years of Experience</div></div>
<div class="abs stat" style="left:380px"><div class="ic on"><svg width="22" height="22" viewBox="0 0 24 24" fill="none" stroke="#fff" stroke-width="1.6"><path d="M12 3l9 16H3z"/></svg></div><div class="num on">100%</div><div class="lbl">Satisfied Customers</div></div>
<div class="abs stat" style="left:620px"><div class="ic"><svg width="24" height="24" viewBox="0 0 24 24" fill="none" stroke="#3a86cf" stroke-width="1.6"><circle cx="12" cy="8" r="3"/><circle cx="5" cy="10" r="2"/><circle cx="19" cy="10" r="2"/><path d="M6 19a6 6 0 0 1 12 0M1 18a4 4 0 0 1 5-3M23 18a4 4 0 0 0-5-3"/></svg></div><div class="num">30+</div><div class="lbl">Team Members</div></div>
<div class="abs stat" style="left:860px"><div class="ic"><svg width="24" height="24" viewBox="0 0 24 24" fill="none" stroke="#3a86cf" stroke-width="1.6"><path d="M12 3l9 5-9 5-9-5z"/><path d="M3 12l9 5 9-5M3 16l9 5 9-5"/></svg></div><div class="num">1650+</div><div class="lbl">Project Completed</div></div>

<!-- SERVICES -->
<section class="abs services"></section>
<div class="abs center eyebrow dash" style="top:1358px">Services</div>
<h2 class="abs center title section-title" style="top:1375px">What We Do</h2>
<p class="abs lead" style="top:1418px;left:375px;width:450px;text-align:center;font-size:10px">Vellora is a leading provider of economical custom software development and staff augmentation services. We specialize in helping companies around the world access top talent in the field of software development at an affordable price, without the hassle and expense of in-house hiring or managing remote employees.</p>

<div class="abs card card-code" role="img" aria-label="Close-up photo of source code on a dark screen"><div class="card-label">CUSTOM SOLUTION</div></div>
<div class="abs card card-staff" role="img" aria-label="Dark photo of a handshake over a keyboard">
  <div class="staff-inner">
    <div class="mark"></div>
    <h3>Staff Augmentation</h3>
    <p>Let Vellora help you supplement your existing software development teams with additional resources and expertise. We provided access to experienced software developers who can work with your in-house teams to help them deliver software projects on time and within budget.</p>
    <div class="btn">Learn More</div>
  </div>
  <svg style="position:absolute;left:143px;bottom:30px" width="16" height="14" viewBox="0 0 16 14" fill="none" stroke="#8fb8e6" stroke-width="1.3"><circle cx="4" cy="3" r="2"/><circle cx="12" cy="3" r="2"/><path d="M1 13l3-6 4 4 4-4 3 6"/></svg>
</div>
<div class="abs card card-support" role="img" aria-label="Photo of hands typing on a laptop showing charts"><div class="card-label">SUPPORT</div></div>
<div class="abs card-badge" style="left:263px"><svg width="14" height="14" viewBox="0 0 24 24" fill="none" stroke="#3a86cf" stroke-width="2"><circle cx="12" cy="12" r="3"/><circle cx="12" cy="12" r="8" stroke-dasharray="3 2"/></svg></div>
<div class="abs card-badge" style="left:903px"><svg width="14" height="14" viewBox="0 0 24 24" fill="none" stroke="#3a86cf" stroke-width="2"><circle cx="12" cy="12" r="9"/><circle cx="12" cy="12" r="4"/><path d="M5.6 5.6l3.6 3.6M18.4 5.6l-3.6 3.6M5.6 18.4l3.6-3.6M18.4 18.4l-3.6-3.6"/></svg></div>

<!-- TESTIMONIALS -->
<section class="abs testimonials" role="img" aria-label="Photo of business colleagues talking in a meeting"><div class="shade"></div></section>
<div class="abs center eyebrow" style="top:2096px;color:#fff;font-size:8px">Testimonials</div>
<h2 class="abs center title" style="top:2114px;font-size:29px;color:#fff;font-weight:600">What Our Clients Say</h2>
<div class="abs avatar" role="img" aria-label="Client portrait"></div>
<p class="abs quote">“Lorem Ipsum is simply dummy text of the printing and typesetting industry. Lorem Ipsum has been the industry's standard dummy text ever since the 1500s, when an unknown printer took a galley of type and scrambled it to make a type specimen book.”</p>
<div class="abs center stars">☆☆☆☆☆</div>
<div class="abs center person"><b>Orin</b><br>Tallis</div>
<svg class="abs" style="top:2272px;left:984px" width="10" height="16" viewBox="0 0 10 16"><path d="M2 2l6 6-6 6" fill="none" stroke="#fff" stroke-width="1.5"/></svg>

<!-- APPROACH -->
<div class="abs center eyebrow dash" style="top:2503px">Approach</div>
<h2 class="abs center title section-title" style="top:2520px">Why Vellora?</h2>
<p class="abs lead" style="top:2564px;left:380px;width:440px;text-align:center;font-size:10px">At Vellora, we are proud to have a team of seasoned IT professionals who understand what it takes to deliver a quality solution.</p>

<div class="abs step" style="left:177px"><div class="ic"><svg width="24" height="24" viewBox="0 0 24 24" fill="none" stroke="#fff" stroke-width="1.6"><circle cx="12" cy="9" r="5"/><path d="M8 13l-2 8 6-3 6 3-2-8"/></svg></div><div class="lbl">Experience</div></div>
<div class="abs step" style="left:318px"><div class="ic"><svg width="24" height="24" viewBox="0 0 24 24" fill="none" stroke="#fff" stroke-width="1.6"><rect x="3" y="4" width="18" height="16" rx="2"/><path d="M3 8h18M10 12l-2 2 2 2M14 12l2 2-2 2"/></svg></div><div class="lbl">Development</div></div>
<div class="abs step" style="left:459px"><div class="ic on"><svg width="24" height="24" viewBox="0 0 24 24" fill="none" stroke="#fff" stroke-width="1.6"><circle cx="12" cy="12" r="3"/><path d="M12 2v3M12 19v3M2 12h3M19 12h3M5 5l2 2M17 17l2 2M5 19l2-2M17 7l2-2"/></svg></div><div class="lbl on">Process</div><svg style="margin-top:8px" width="8" height="5" viewBox="0 0 8 5"><path d="M1 1l3 3 3-3" fill="none" stroke="#3a86cf"/></svg></div>
<div class="abs step" style="left:601px"><div class="ic"><svg width="24" height="24" viewBox="0 0 24 24" fill="none" stroke="#fff" stroke-width="1.6"><circle cx="12" cy="12" r="9"/><circle cx="12" cy="12" r="4"/></svg></div><div class="lbl">Solution</div></div>
<div class="abs step" style="left:742px"><div class="ic"><svg width="24" height="24" viewBox="0 0 24 24" fill="none" stroke="#fff" stroke-width="1.6"><circle cx="12" cy="12" r="4"/><circle cx="12" cy="12" r="8" stroke-dasharray="4 2"/></svg></div><div class="lbl">Support</div></div>
<div class="abs step" style="left:883px"><div class="ic"><svg width="24" height="24" viewBox="0 0 24 24" fill="none" stroke="#fff" stroke-width="1.6"><path d="M2 12l5-5 5 3 5-3 5 5-7 7-3-3-3 3z"/></svg></div><div class="lbl">Partner</div></div>

<h3 class="abs center" style="top:2744px;font-size:15px;font-weight:600;color:#1d1d1f">Improve Processes And Drive Results</h3>
<p class="abs lead" style="top:2771px;left:230px;width:740px;text-align:center;font-size:10px">Our team members are committed to delivering excellence in everything they do, and they are always looking for ways to improve processes and drive results. We believe that by working together as a team and leveraging each other's strengths and expertise, we can deliver the best possible solutions for our clients.</p>

<!-- TEAM -->
<section class="abs team"></section>
<div class="abs center eyebrow dash" style="top:2950px">Team</div>
<h2 class="abs center title section-title" style="top:2967px">Vellora Leadership</h2>
<p class="abs lead" style="top:3010px;left:375px;width:450px;text-align:center;font-size:10px">Our team of highly skilled software developers has extensive experience working with a wide range of technologies, including web and mobile development, cloud computing, and data analytics.</p>

<div class="abs member" style="left:271px"><div class="pic" role="img" aria-label="Portrait of team leader" style="background:linear-gradient(160deg,#e8e8e8,#b9b3ad)"></div><div class="name">Dario Fenwick</div><div class="role">Title</div></div>
<div class="abs member" style="left:500px"><div class="pic" role="img" aria-label="Portrait of team leader with blue overlay" style="background:linear-gradient(160deg,#2a79d0,#0d4f9f)"></div><div class="name on">Lucas Brenner</div><div class="role">Title</div></div>
<div class="abs bio">View Bio</div>
<div class="abs member" style="left:729px"><div class="pic" role="img" aria-label="Grey placeholder silhouette for a future team member" style="background:linear-gradient(180deg,#e2e2e2,#c4c4c4)"></div><div class="name">Maybe You</div><div class="role">Join Our Team</div></div>

<div class="abs center eyebrow" style="top:3390px;font-size:8px">Certifications</div>
<div class="abs cert" style="left:158px"><div class="shape" style="width:60px;height:26px"></div></div>
<div class="abs cert" style="left:338px"><div class="shape" style="width:28px;height:28px;border-radius:50%"></div></div>
<div class="abs cert on" style="left:518px"><div class="shape" style="width:54px;height:26px;background:#9aa0a8"></div></div>
<div class="abs cert" style="left:699px"><div class="shape" style="width:28px;height:28px;border-radius:50%"></div></div>
<div class="abs cert" style="left:879px"><div class="shape" style="width:72px;height:18px"></div></div>

<!-- CTA -->
<section class="abs cta" role="img" aria-label="Photo looking up at glass office towers against the sky"></section>
<div class="abs center eyebrow" style="top:3661px;color:#fff;font-size:8px">Get Started</div>
<h2 class="abs center title" style="top:3680px;font-size:29px;color:#fff;font-weight:600">We're Here To Help</h2>
<p class="abs lead" style="top:3726px;left:360px;width:480px;text-align:center;color:#fff;font-size:10px">If you have any questions or requests about our company or the services we provide, please call or email us, or use the form below.</p>
<div class="abs btn" style="top:3778px;left:517px;width:167px;height:30px">&#9993;&nbsp; Contact Us Today!</div>

<!-- FOOTER -->
<footer class="abs footer"></footer>
<div class="abs foot-brand"><span class="brand-dot"></span><span class="brand-name">VELLORA CONSULTING</span></div>
<div class="abs center copy">© COPYRIGHT 2022 VELLORA CONSULTING. ALL RIGHTS RESERVED</div>
<div class="abs center foot-links"><span>CAREERS</span><span>PRIVACY POLICY</span></div>
<div class="social"><i aria-label="Professional network"></i><i class="on" aria-label="Social page"></i><i aria-label="Microblog"></i></div>
<svg class="abs" style="top:4158px;left:596px" width="8" height="5" viewBox="0 0 8 5"><path d="M1 4l3-3 3 3" fill="none" stroke="#fff"/></svg>

</body>
</html>
```